Physiotherapy business needs patient information graphic redesign

We have existing graphics that we need redesigned to add some artistic flare. The images must remain professional and suitable for a healthcare setting but some artistic flare is need to add interest to the graphics so that patients are able to engage more easily with the info sheet. Graphics include "INS", "graded activity", "pacing I", "pacing II" and "sleep"

Target Market(s)

Practitioners and patients with pain

Industry/Entity Type

Business

Font styles to use
Sans Serif

Colors
3176b5
9bcb3b
ec1f27

Requirements
Must have
• The ability to communicate the message in the graphic
• Artistic flair
• Retain professionalism
Nice to have
• Unique creativity that distinguishes our product
• Matching with our logo (attached). Does not have to be the same colours or style/font but still should fit with the logo stylistically
Should not have
• A similar boring and flat feel as the existing graphics

```html
<!DOCTYPE html>
<html lang="en">
<head>
<meta charset="utf-8">
<title>Pacing and Graded Activity</title>
<link href="https://fonts.googleapis.com/css2?family=Montserrat:wght@500;700&display=swap" rel="stylesheet">
<style>
  :root {
    --red: #e3202a;
    --blue: #0e80c2;
    --green: #8cc43f;
    --pale-green: #d3e6b0;
    --axis: #cfcfcf;
    --axis-label: #9a9a9a;
    --ink: #222222;
    --guide: #c7dcef;
    --bg: #ffffff;
  }
  html, body { margin: 0; padding: 0; overflow: hidden; background: var(--bg); }
  .canvas { width: 901px; height: 1200px; display: block; }
  .axis { stroke: var(--axis); stroke-width: 5; fill: none; }
  .axis-label { font-family: "Montserrat", sans-serif; font-weight: 500; font-size: 17px; fill: var(--axis-label); }
  .warning-label { font-family: "Montserrat", sans-serif; font-weight: 700; font-size: 24px; fill: var(--red); }
  .rest-label { font-family: "Montserrat", sans-serif; font-weight: 700; font-size: 23px; fill: var(--green); }
  .baseline-label { font-family: "Montserrat", sans-serif; font-weight: 700; font-size: 24px; fill: var(--blue); }
  .chart-label { font-family: "Montserrat", sans-serif; font-weight: 500; font-size: 24px; fill: var(--ink); }
  .achieved-label { font-family: "Montserrat", sans-serif; font-weight: 700; font-size: 24px; fill: var(--blue); }
  .activity-line { fill: none; stroke-width: 12; stroke-linejoin: miter; }
  .baseline-line { fill: none; stroke: var(--blue); stroke-width: 17; stroke-linecap: round; }
  .guide { fill: none; stroke: var(--guide); stroke-width: 2; }
  .steps { fill: none; stroke: var(--pale-green); stroke-width: 12; }
  .pain-line { fill: none; stroke-width: 17; stroke-linecap: round; }
</style>
</head>
<body>
<svg class="canvas" viewBox="0 0 1134 1500" preserveAspectRatio="none" xmlns="http://www.w3.org/2000/svg">
  <defs>
    <linearGradient id="boom-bust-1" gradientUnits="userSpaceOnUse" x1="0" y1="412" x2="0" y2="185">
      <stop offset="0" stop-color="#8cc43f"/>
      <stop offset="0.45" stop-color="#0e80c2"/>
      <stop offset="1" stop-color="#e3202a"/>
    </linearGradient>
    <linearGradient id="boom-bust-2" gradientUnits="userSpaceOnUse" x1="0" y1="885" x2="0" y2="658">
      <stop offset="0" stop-color="#8cc43f"/>
      <stop offset="0.45" stop-color="#0e80c2"/>
      <stop offset="1" stop-color="#e3202a"/>
    </linearGradient>
    <linearGradient id="goal-bar" x1="0" y1="0" x2="1" y2="0">
      <stop offset="0" stop-color="#0e80c2" stop-opacity="0"/>
      <stop offset="1" stop-color="#0e80c2"/>
    </linearGradient>
    <linearGradient id="pain-fade" gradientUnits="userSpaceOnUse" x1="380" y1="0" x2="900" y2="0">
      <stop offset="0" stop-color="#e3202a"/>
      <stop offset="0.5" stop-color="#0e80c2"/>
      <stop offset="1" stop-color="#8cc43f"/>
    </linearGradient>
  </defs>

  <!-- Boom and bust cycle -->
  <g class="chart chart-boom-bust">
    <text class="axis-label" x="130" y="138" text-anchor="end">NORMAL</text>
    <text class="axis-label" x="130" y="156" text-anchor="end">ACTIVITY</text>
    <text class="axis-label" x="130" y="410" text-anchor="end">UNDER</text>
    <text class="axis-label" x="130" y="428" text-anchor="end">ACTIVITY</text>
    <path class="axis" d="M139 82 V470 H1071"/>
    <path class="activity-line" stroke="url(#boom-bust-1)" d="M183 412 H262 L342 185 L422 412 H527 L607 185 L687 412 H792 L872 185 L952 412 H1031"/>
    <g class="warnings">
      <g transform="translate(342 165)"><path d="M0 -14 L14 12 H-14 Z" fill="var(--red)"/><rect x="-1.8" y="-6" width="3.6" height="10" fill="#fff"/><circle cx="0" cy="8" r="2" fill="#fff"/></g>
      <g transform="translate(607 165)"><path d="M0 -14 L14 12 H-14 Z" fill="var(--red)"/><rect x="-1.8" y="-6" width="3.6" height="10" fill="#fff"/><circle cx="0" cy="8" r="2" fill="#fff"/></g>
      <g transform="translate(872 165)"><path d="M0 -14 L14 12 H-14 Z" fill="var(--red)"/><rect x="-1.8" y="-6" width="3.6" height="10" fill="#fff"/><circle cx="0" cy="8" r="2" fill="#fff"/></g>
      <text class="warning-label" x="342" y="146" text-anchor="middle">Overdo Activity</text>
      <text class="warning-label" x="607" y="146" text-anchor="middle">Overdo Activity</text>
      <text class="warning-label" x="872" y="146" text-anchor="middle">Overdo Activity</text>
    </g>
    <g class="rests" fill="var(--green)">
      <text class="rest-label" x="473" y="364" text-anchor="middle">Rest</text>
      <g transform="translate(450 371)"><rect x="0" y="0" width="5" height="30"/><rect x="0" y="18" width="48" height="5"/><rect x="43" y="18" width="5" height="12"/><circle cx="13" cy="9" r="4.5"/><rect x="19" y="8" width="29" height="7" rx="2"/></g>
      <text class="rest-label" x="738" y="364" text-anchor="middle">Rest</text>
      <g transform="translate(715 371)"><rect x="0" y="0" width="5" height="30"/><rect x="0" y="18" width="48" height="5"/><rect x="43" y="18" width="5" height="12"/><circle cx="13" cy="9" r="4.5"/><rect x="19" y="8" width="29" height="7" rx="2"/></g>
    </g>
  </g>

  <!-- Stable baseline -->
  <g class="chart chart-baseline">
    <text class="axis-label" x="130" y="611" text-anchor="end">NORMAL</text>
    <text class="axis-label" x="130" y="629" text-anchor="end">ACTIVITY</text>
    <text class="axis-label" x="130" y="883" text-anchor="end">UNDER</text>
    <text class="axis-label" x="130" y="901" text-anchor="end">ACTIVITY</text>
    <path class="axis" d="M139 555 V942 H1071"/>
    <path class="activity-line" stroke="url(#boom-bust-2)" d="M183 885 H262 L342 658 L422 885 H527 L607 658 L687 885 H792 L872 658 L952 885 H1031"/>
    <path class="baseline-line" d="M189 777 C300 762 400 792 490 788 C560 785 580 770 640 772 C700 775 760 795 820 786 C880 777 930 765 1026 777"/>
    <path class="guide" d="M474 757 V612 H488 M740 757 V612 H727"/>
    <circle cx="474" cy="758" r="3.5" fill="var(--guide)"/>
    <circle cx="740" cy="758" r="3.5" fill="var(--guide)"/>
    <text class="baseline-label" x="607" y="619" text-anchor="middle">A Stable Baseline</text>
  </g>

  <!-- Graded activity -->
  <g class="chart chart-graded">
    <text class="axis-label" x="130" y="1084" text-anchor="end">NORMAL</text>
    <text class="axis-label" x="130" y="1102" text-anchor="end">ACTIVITY</text>
    <text class="axis-label" x="130" y="1356" text-anchor="end">UNDER</text>
    <text class="axis-label" x="130" y="1374" text-anchor="end">ACTIVITY</text>
    <path class="axis" d="M139 1028 V1415 H1071"/>
    <text class="chart-label" x="183" y="1053">Your Goals</text>
    <rect x="183" y="1060" width="795" height="28" fill="url(#goal-bar)"/>
    <text class="achieved-label" x="970" y="1054" text-anchor="end">ACHIEVED!</text>
    <circle cx="1003" cy="1058" r="25" fill="var(--green)"/>
    <path class="steps" d="M183 1372 H310 V1336 H408 V1300 H505 V1264 H603 V1228 H700 V1192 H797 V1156 H895 V1120 H1030"/>
    <path class="pain-line" stroke="url(#pain-fade)" d="M190 1134 C300 1133 370 1136 410 1143 C520 1165 620 1225 720 1275 C800 1315 850 1332 900 1338 C950 1344 990 1347 1026 1352"/>
    <text class="chart-label" x="184" y="1172">Pain Levels</text>
    <text class="chart-label" x="325" y="1373">Gradede Activity/</text>
    <text class="chart-label" x="325" y="1398">Exercise</text>
  </g>
</svg>
</body>
</html>
```